Business card logo

Hello, I would like a business card for my law firm with a logo composed of my initials "CV". The logo is intended to appear on my business card, my letterhead, envelope and documents from my office. My first and last name (Camille Vautrin) and "Lawyer" must appear next to the logo. I would like the logo and the characters to be in golden color on a dark background (example black, navy blue). I would especially like a refined work on the logo which should be composed of the letters J and R.

```html
<!DOCTYPE html>
<html lang="en">
<head>
<meta charset="utf-8">
<title>Camille Vautrin – Business Card</title>
<link rel="stylesheet" href="https://fonts.googleapis.com/css2?family=Tinos:wght@400&family=Work+Sans:wght@400;500;600&display=swap">
<style>
  :root {
    --page-bg: #141414;
    --card-bg: #1c1c1c;
    --card-edge: #2a2a2a;
    --gold: #cfa95e;
    --gold-soft: #b8944f;
    --serif: "Tinos", "Times New Roman", serif;
    --sans: "Work Sans", Arial, sans-serif;
  }
  * { margin: 0; padding: 0; box-sizing: border-box; }
  html, body {
    width: 1200px; height: 900px; overflow: hidden;
    background: var(--page-bg);
  }
  .sheet {
    width: 1200px; height: 900px;
    display: flex; flex-direction: column; align-items: center; justify-content: center;
    gap: 40px;
  }
  .card {
    width: 700px; height: 400px;
    background: var(--card-bg);
    border: 1px solid var(--card-edge);
    position: relative;
  }
  .card--front {
    display: flex; align-items: center; justify-content: center;
  }
  .brand {
    display: flex; flex-direction: column; align-items: center;
  }
  .brand-name {
    font-family: var(--serif);
    font-weight: 400;
    color: var(--gold);
    text-transform: uppercase;
    letter-spacing: 0.04em;
    white-space: nowrap;
  }
  .brand-role {
    font-family: var(--serif);
    font-weight: 400;
    color: var(--gold);
    text-transform: uppercase;
    letter-spacing: 0.3em;
    white-space: nowrap;
  }
  .card--front .brand-name { font-size: 46px; }
  .card--front .brand-role { font-size: 18px; margin-top: 8px; }
  .card--back {
    display: flex; align-items: center;
  }
  .back-brand {
    width: 320px;
    display: flex; justify-content: center;
  }
  .back-brand .brand-name { font-size: 27px; }
  .back-brand .brand-role { font-size: 13px; margin-top: 6px; }
  .divider {
    width: 1px; height: 190px;
    background: var(--gold-soft);
  }
  .contact {
    padding-left: 42px;
    font-family: var(--sans);
    color: var(--gold);
  }
  .contact-name {
    font-size: 26px; font-weight: 600; letter-spacing: 0.06em;
    text-transform: uppercase;
  }
  .contact-role {
    font-size: 15px; color: var(--gold-soft); margin-top: 2px;
  }
  .contact-address {
    font-size: 17px; line-height: 1.4; margin-top: 20px; letter-spacing: 0.03em;
  }
  .contact-list {
    list-style: none; margin-top: 16px;
    font-size: 17px; letter-spacing: 0.03em; line-height: 1.5;
  }
  .contact-list li { display: flex; align-items: center; gap: 10px; }
  .contact-list svg { width: 13px; height: 13px; flex: none; }
</style>
</head>
<body>
<main class="sheet">
  <section class="card card--front">
    <div class="brand">
      <span class="brand-name">Camille Vautrin</span>
      <span class="brand-role">Lawyer</span>
    </div>
  </section>

  <section class="card card--back">
    <div class="back-brand">
      <div class="brand">
        <span class="brand-name">Camille Vautrin</span>
        <span class="brand-role">Lawyer</span>
      </div>
    </div>
    <div class="divider"></div>
    <div class="contact">
      <p class="contact-name">Daniel Forster</p>
      <p class="contact-role">Director</p>
      <p class="contact-address">418 Harbor St.<br>Millbrook, OH 45210</p>
      <ul class="contact-list">
        <li>
          <svg viewBox="0 0 16 16" aria-hidden="true"><path fill="#cfa95e" d="M3.6 1.2l2.3 2.6-1.3 1.9c.9 2 2.6 3.7 4.6 4.6l1.9-1.3 2.6 2.3-1.4 2.2C7.2 15 1 8.8 1.4 2.6z"/></svg>
          555-014-2290
        </li>
        <li>
          <svg viewBox="0 0 16 16" aria-hidden="true"><rect x="1.5" y="3.5" width="13" height="9" fill="none" stroke="#cfa95e" stroke-width="1.5"/><path d="M1.5 3.5L8 9l6.5-5.5" fill="none" stroke="#cfa95e" stroke-width="1.5"/></svg>
          info@CamilleVautrin.com
        </li>
        <li>
          <svg viewBox="0 0 16 16" aria-hidden="true"><g fill="none" stroke="#cfa95e" stroke-width="1.3"><circle cx="8" cy="8" r="6.5"/><ellipse cx="8" cy="8" rx="2.8" ry="6.5"/><path d="M1.5 8h13M2.5 4.8h11M2.5 11.2h11"/></g></svg>
          www.CamilleVautrin.com
        </li>
      </ul>
    </div>
  </section>
</main>
</body>
</html>
```